Birchline Septic Solutions

Would like to see some single sided ones but would also like to see some double sided with one sided only being the logo. Owners name is Tom Halvick. Phone number is 555-214-0387
Services are pumping, inspections, installs, and repairs

Contact Information for Business Card

555-241-0387 Tom Halvick Greenfield, OH

```html
<!DOCTYPE html>
<html lang="en">
<head>
<meta charset="utf-8">
<title>Birchline Septic Solutions – Business Cards</title>
<link href="https://fonts.googleapis.com/css2?family=Raleway:wght@400;600;800&display=swap" rel="stylesheet">
<style>
  :root {
    --bg: #e6e7e9;
    --card-white: #ffffff;
    --card-black: #0d0d0d;
    --ink: #111111;
    --teal: #19bfb8;
    --rule: #8a8a8a;
  }
  * { box-sizing: border-box; margin: 0; padding: 0; }
  html, body {
    width: 1200px; height: 1200px; overflow: hidden;
    background: var(--bg);
    font-family: "Raleway", sans-serif;
  }
  .sheet {
    position: relative; width: 1200px; height: 1200px;
    display: flex; flex-direction: column; align-items: center; justify-content: center; gap: 36px;
  }
  .card {
    position: relative; width: 960px; height: 548px;
    border-radius: 44px; overflow: hidden;
    box-shadow: 0 10px 30px rgba(0,0,0,0.18);
  }
  .card--front { background: var(--card-white); }
  .card--back { background: var(--card-black); display: flex; align-items: center; justify-content: center; }

  .brand { text-align: center; font-weight: 800; letter-spacing: 0.02em; line-height: 1; }
  .brand__name { display: block; font-size: 96px; }
  .brand__tag { display: block; font-size: 30px; letter-spacing: 0.32em; margin-top: 14px; }
  .card--front .brand { position: absolute; left: 200px; top: 92px; width: 480px; color: var(--ink); }
  .card--front .brand__name { font-size: 86px; }
  .card--front .brand__tag { font-size: 26px; }
  .card--back .brand { color: #ffffff; }

  .person { position: absolute; left: 240px; top: 396px; }
  .person__name { font-size: 46px; font-weight: 600; color: var(--teal); letter-spacing: -0.02em; line-height: 1; }
  .person__role { font-size: 32px; font-weight: 400; color: var(--ink); letter-spacing: -0.02em; margin-top: 2px; }

  .divider { position: absolute; left: 548px; top: 300px; width: 1px; height: 86px; background: var(--rule); }

  .contact { position: absolute; left: 584px; top: 240px; list-style: none; }
  .contact__item { display: flex; align-items: center; gap: 12px; height: 42px; font-size: 22px; color: var(--ink); white-space: nowrap; }
  .contact__item--phone { font-size: 28px; }
  .contact__icon { width: 24px; height: 24px; flex: none; }

  .bands { position: absolute; left: 0; bottom: 0; width: 960px; height: 80px; }
</style>
</head>
<body>
<main class="sheet">

  <section class="card card--front" aria-label="Business card front">
    <div class="brand">
      <span class="brand__name">BIRCHLINE</span>
      <span class="brand__tag">SEPTIC SOLUTIONS</span>
    </div>

    <div class="person">
      <p class="person__name">TOM HALVICK</p>
      <p class="person__role">OWNER</p>
    </div>

    <div class="divider"></div>

    <ul class="contact">
      <li class="contact__item contact__item--phone">
        <svg class="contact__icon" viewBox="0 0 24 24"><path fill="var(--teal)" d="M6.6 10.8a15.1 15.1 0 0 0 6.6 6.6l2.2-2.2a1 1 0 0 1 1-.25 11.4 11.4 0 0 0 3.6.57 1 1 0 0 1 1 1V20a1 1 0 0 1-1 1A17 17 0 0 1 3 4a1 1 0 0 1 1-1h3.5a1 1 0 0 1 1 1c0 1.25.2 2.450.57 3.6a1 1 0 0 1-.25 1z"/></svg>
        555-214-0387
      </li>
      <li class="contact__item">
        <svg class="contact__icon" viewBox="0 0 24 24"><rect x="2" y="5" width="20" height="14" rx="1" fill="var(--teal)"/><path d="M2.5 6l9.5 7 9.5-7" fill="none" stroke="#fff" stroke-width="1.6"/></svg>
        office@birchlineseptic.com
      </li>
      <li class="contact__item">
        <svg class="contact__icon" viewBox="0 0 24 24" fill="none" stroke="var(--teal)" stroke-width="1.8"><circle cx="12" cy="12" r="10"/><ellipse cx="12" cy="12" rx="4.5" ry="10"/><path d="M2 12h20M4 7h16M4 17h16"/></svg>
        www.birchlineseptic.com
      </li>
    </ul>

    <svg class="bands" viewBox="0 0 960 80" preserveAspectRatio="none" aria-hidden="true">
      <rect x="0" y="58" width="640" height="22" fill="var(--teal)"/>
      <polygon points="646,80 654,36 960,36 960,80" fill="var(--ink)"/>
    </svg>
  </section>

  <section class="card card--back" aria-label="Business card back">
    <div class="brand">
      <span class="brand__name">BIRCHLINE</span>
      <span class="brand__tag">SEPTIC SOLUTIONS</span>
    </div>
  </section>

</main>
</body>
</html>
```